Stonebay Towing Business Card

Towing
Accident towing
Mechanical breakdown
Insurance, salvage and recovery
4wd off road towing
Light & Heavy towing
8347 2516
24 hour business 7 days

Logo can be whole size on front

Industry/Entity Type

Towing/ transport

Contact Information for Business Card

The above

```html
<!DOCTYPE html>
<html lang="en">
<head>
<meta charset="utf-8">
<title>Stonebay Towing Business Card</title>
<link rel="stylesheet" href="https://fonts.googleapis.com/css2?family=Exo+2:ital,wght@1,800&family=Noto+Serif:wght@400;700&display=swap">
<style>
  :root {
    --stage: #000000;
    --paper: #ffffff;
    --brand-red: #d42027;
    --brand-red-soft: rgba(212, 32, 39, 0.15);
    --ink: #231f20;
  }
  html, body {
    margin: 0;
    padding: 0;
    width: 1200px;
    height: 1200px;
    overflow: hidden;
    background: var(--stage);
  }
  .stage {
    position: relative;
    width: 1200px;
    height: 1200px;
    background: var(--stage);
  }
  .card {
    position: absolute;
    left: 222px;
    width: 756px;
    height: 432px;
    background: var(--paper);
    overflow: hidden;
  }
  .card--back { top: 135px; }
  .card--front { top: 632px; }

  .brand-name {
    position: absolute;
    margin: 0;
    font-family: "Noto Serif", serif;
    font-weight: 700;
    color: var(--brand-red);
    line-height: 1.05;
  }
  .card--back .brand-name {
    left: 45px;
    top: 170px;
    width: 280px;
    font-size: 36px;
  }
  .card--front .brand-name {
    left: 40px;
    top: 62px;
    width: 460px;
    font-size: 66px;
  }

  .services {
    position: absolute;
    left: 378px;
    top: 78px;
    margin: 0;
    padding: 0;
    list-style: none;
    font-family: "Noto Serif", serif;
    font-weight: 400;
    font-size: 15.5px;
    letter-spacing: 1.4px;
    color: var(--ink);
  }
  .services li {
    height: 38px;
    line-height: 22px;
  }

  .contact {
    position: absolute;
    left: 377px;
    top: 312px;
    margin: 0;
    font-family: "Exo 2", sans-serif;
    font-style: italic;
    font-weight: 800;
  }
  .contact__phone {
    display: block;
    font-size: 40px;
    line-height: 40px;
    color: var(--brand-red);
    letter-spacing: 6px;
  }
  .contact__hours {
    display: block;
    font-size: 27px;
    line-height: 30px;
    color: var(--ink);
    letter-spacing: 4.5px;
  }

  .wave-area {
    position: absolute;
    left: 0;
    top: 262px;
    width: 756px;
    height: 170px;
    background: linear-gradient(to bottom, var(--brand-red-soft), var(--brand-red) 60%);
  }
</style>
</head>
<body>
<main class="stage">
  <section class="card card--back" aria-label="Business card, back">
    <h2 class="brand-name">Stonebay Towing</h2>
    <ul class="services">
      <li>TOWING</li>
      <li>ACCIDENT TOWING</li>
      <li>MECHANICAL BREAKDOWN</li>
      <li>INSURANCE, SALVAGE AND RECOVERY</li>
      <li>4WD OFF ROAD TOWING</li>
      <li>LIGHT &amp; HEAVY TOWING</li>
    </ul>
    <p class="contact">
      <span class="contact__phone">8347 2516</span>
      <span class="contact__hours">24/7 BUSINESS</span>
    </p>
  </section>

  <section class="card card--front" aria-label="Business card, front">
    <h1 class="brand-name">Stonebay Towing</h1>
    <div class="wave-area" role="img" aria-label="Decorative red swoosh band across the lower edge of the card"></div>
  </section>
</main>
</body>
</html>
```